R J Security Flyer - Security Based Company

Security company offering installation of CCTV and Intruder alarm systems mainly but not limited to home alarms. Feel free to be creative

Target Market(s)

Residential and Commercial properties, Facility Managers, local business

Requirements
Must have
• smart professional finish, logo and latest up to date pictures if on kit

```html
<!DOCTYPE html>
<html lang="en">
<head>
<meta charset="utf-8">
<title>R J Security Systems Flyer</title>
<link rel="stylesheet" href="https://fonts.googleapis.com/css2?family=Exo+2:ital,wght@0,300;0,400;0,600;0,700;1,300;1,400&family=Open+Sans:wght@400;600&display=swap">
<style>
:root{
  --orange:#e8632a;
  --orange-light:#f07a35;
  --navy:#1f2d47;
  --navy-deep:#17223a;
  --white:#ffffff;
  --ink:#3b3b3b;
  --backdrop:#7b7b7b;
  --photo-dark-a:#2b2522;
  --photo-dark-b:#4d3d33;
  --photo-light-a:#e9ecef;
  --photo-light-b:#b9c0c7;
}
*{margin:0;padding:0;box-sizing:border-box}
html,body{width:1200px;height:849px;overflow:hidden;background:var(--backdrop)}
.stage{position:relative;width:1200px;height:849px}
.page{position:absolute;top:65px;width:508px;height:718px;overflow:hidden;background:var(--white)}
.page--front{left:72px}
.page--back{left:620px}
.page svg.shapes{position:absolute;left:0;top:0}
.t{position:absolute;font-family:"Exo 2",sans-serif;line-height:1.05;white-space:nowrap}

/* front headline */
.front-title{left:200px;width:310px;text-align:center;top:34px;font-size:26px;font-weight:300;color:var(--white)}
.front-rule{position:absolute;left:318px;top:70px;width:80px;height:2px;background:var(--white)}
.front-head{left:200px;width:310px;text-align:center;font-size:23px;color:var(--orange)}
.front-head.bold{font-weight:700}
.front-head.light{font-weight:300}
.front-head.white{color:var(--white);font-weight:700;font-size:27px}

.brand{left:0;width:160px;text-align:center;font-size:17px;font-weight:700;color:var(--navy);line-height:1.15}

.ask{left:240px;width:260px;text-align:center}
.ask.orange{color:var(--orange)}
.ask.navy{color:var(--navy)}

.bullet{position:absolute;font-family:"Open Sans",sans-serif;font-size:7.4px;line-height:1.25;color:var(--ink);padding-left:14px}
.bullet::before{content:"";position:absolute;left:0;top:1px;width:6px;height:6px;background:var(--orange);box-shadow:1px 1px 0 var(--navy)}

.cta{position:absolute;left:92px;top:607px;width:400px;height:25px;background:var(--orange);clip-path:polygon(14px 0,100% 0,100% 100%,0 100%);color:var(--white);font-family:"Open Sans",sans-serif;font-size:9.4px;line-height:1.15;text-align:right;padding:2px 10px 0 20px}

.contact{position:absolute;font-family:"Open Sans",sans-serif;font-size:9.4px;color:var(--navy);white-space:nowrap;display:flex;align-items:center;gap:6px}
.contact svg{flex:none}
.badge-caption{position:absolute;left:40px;top:682px;width:58px;text-align:center;font-family:Georgia,serif;font-size:6.6px;font-weight:700;color:var(--navy);line-height:1.15}
.review-name{left:380px;top:654px;font-size:15px;font-weight:600;color:var(--orange)}
.review-tag{left:418px;top:671px;font-family:"Open Sans",sans-serif;font-size:6.4px;color:var(--navy)}

/* back */
.back-head{left:230px;width:278px;text-align:center;color:var(--navy)}
.benefits-title{right:36px;top:201px;font-size:17px;font-weight:300;font-style:italic;color:var(--white)}
.benefit{position:absolute;right:22px;display:flex;align-items:center;gap:6px;font-family:"Open Sans",sans-serif;font-size:7.4px;color:var(--white);white-space:nowrap}
.benefit .dash{width:6px;height:1px;background:var(--white)}
.benefit svg{flex:none}
.cloud-copy{position:absolute;left:24px;top:373px;width:450px;font-family:"Open Sans",sans-serif;font-size:6.1px;line-height:1.3;color:var(--white);text-align:right}
.always{right:24px;text-align:right}
</style>
</head>
<body>
<div class="stage">

  <!-- FRONT PAGE -->
  <section class="page page--front">
    <svg class="shapes" width="508" height="718" viewBox="0 0 508 718">
      <defs>
        <linearGradient id="roomPhoto" x1="0" y1="0" x2="1" y2="1">
          <stop offset="0" stop-color="var(--photo-dark-a)"/>
          <stop offset="1" stop-color="var(--photo-dark-b)"/>
        </linearGradient>
        <linearGradient id="lightPhoto" x1="0" y1="0" x2="1" y2="1">
          <stop offset="0" stop-color="var(--photo-light-a)"/>
          <stop offset="1" stop-color="var(--photo-light-b)"/>
        </linearGradient>
        <linearGradient id="phonePhoto" x1="0" y1="0" x2="1" y2="1">
          <stop offset="0" stop-color="#c9b9a8"/>
          <stop offset="1" stop-color="#6f5e52"/>
        </linearGradient>
      </defs>
      <rect width="508" height="718" fill="var(--orange)"/>
      <path d="M222,0 H508 V250 C360,258 260,300 220,380 C196,320 168,262 176,184 C184,104 226,44 222,0 Z" fill="var(--navy)"/>
      <path role="img" aria-label="Photo of a dim modern interior with a wall alarm panel" d="M236,0 H508 V250 C360,258 262,296 226,360 C206,310 184,258 192,186 C200,110 240,48 236,0 Z" fill="url(#roomPhoto)"/>
      <rect role="img" aria-label="Photo of a white CCTV bullet camera on a wall bracket" x="0" y="14" width="200" height="176" rx="8" fill="url(#lightPhoto)" opacity="0.92"/>
      <path d="M508,250 C360,258 260,300 220,380 C185,460 110,560 0,600 V718 H508 Z" fill="var(--navy)"/>
      <path d="M508,276 C380,284 300,324 265,396" fill="none" stroke="var(--orange)" stroke-width="7"/>
      <path d="M508,282 C380,290 300,330 265,400 C230,480 150,590 0,640 V718 H508 Z" fill="var(--white)"/>
      <rect x="0" y="709" width="508" height="9" fill="var(--navy)"/>
      <circle cx="208" cy="298" r="55" fill="var(--white)"/>
      <circle cx="208" cy="298" r="51" fill="var(--orange)"/>
      <circle role="img" aria-label="3D plan of a house with security sensors" cx="208" cy="298" r="46" fill="url(#lightPhoto)"/>
      <circle cx="164" cy="406" r="55" fill="var(--white)"/>
      <circle cx="164" cy="406" r="51" fill="var(--orange)"/>
      <circle role="img" aria-label="Photo of a hand using a security app on a phone" cx="164" cy="406" r="46" fill="url(#phonePhoto)"/>
      <circle cx="76" cy="482" r="55" fill="var(--white)"/>
      <circle cx="76" cy="482" r="51" fill="var(--orange)"/>
      <circle role="img" aria-label="Photo of an alarm keypad" cx="76" cy="482" r="46" fill="url(#lightPhoto)"/>
      <circle cx="310" cy="272" r="40" fill="var(--orange)"/>
      <circle role="img" aria-label="Photo of a white dome security camera" cx="310" cy="266" r="30" fill="url(#lightPhoto)"/>
      <circle cx="68" cy="655" r="21" fill="none" stroke="var(--navy)" stroke-width="3"/>
      <circle cx="68" cy="655" r="14" fill="var(--navy)"/>
    </svg>

    <div class="t front-title">R J Security Systems</div>
    <div class="front-rule"></div>
    <div class="t front-head bold" style="top:88px">Can help to carefully</div>
    <div class="t front-head light" style="top:117px">choose the right</div>
    <div class="t front-head white" style="top:147px">SECURITY SYSTEM</div>
    <div class="t front-head bold" style="top:180px">for you.</div>

    <div class="t brand" style="top:302px">R J SECURITY<br>SYSTEMS</div>

    <div class="t ask orange" style="top:332px;font-size:19px;font-weight:600">Are you</div>
    <div class="t ask navy" style="top:353px;font-size:29px;font-weight:600">LOOKING</div>
    <div class="t ask orange" style="top:385px;font-size:19px;font-weight:300">to keep you or your</div>
    <div class="t ask navy" style="top:407px;font-size:18px;font-weight:700">PREMISES SAFE?</div>

    <div class="bullet" style="left:276px;top:445px;width:224px">We install, maintain and repair all intruder alarms, CCTV, intercom and access control</div>
    <div class="bullet" style="left:260px;top:471px;width:240px">View, control and manage your security systems anywhere in the world with smartphone apps</div>
    <div class="bullet" style="left:242px;top:497px;width:258px">Feel at ease with monitoring services and police response tailored to suit you and your business</div>
    <div class="bullet" style="left:222px;top:523px;width:278px">We can takeover any existing security system and offer maintenance checks to guarantee the best performance for you and your premises</div>
    <div class="bullet" style="left:194px;top:549px;width:306px">We understand that being security conscious is ever increasing, protecting your property and family is a number one priority</div>
    <div class="bullet" style="left:168px;top:575px;width:332px">Our fully insured and accredited team offer quality, safety and cost efficiency throughout and whole process</div>

    <div class="cta">If you are looking to improve the security in your home, office or commercial property then call a member of our team today for a free quote.</div>

    <div class="contact" style="left:196px;top:640px">
      <svg width="10" height="10" viewBox="0 0 10 10"><path d="M2,0.5 L3.8,2.6 L2.8,3.8 C3.5,5.3 4.7,6.5 6.2,7.2 L7.4,6.2 L9.5,8 L8.3,9.5 C4.2,9.2 0.8,5.8 0.5,1.7 Z" fill="var(--orange)"/></svg>
      01632 480517</div>
    <div class="contact" style="left:140px;top:655px">
      <svg width="11" height="8" viewBox="0 0 11 8"><rect width="11" height="8" fill="var(--orange)"/><path d="M0,0 L5.5,4.5 L11,0" fill="none" stroke="var(--white)" stroke-width="1"/></svg>
      operations@rjsecuritysystems.co.uk</div>
    <div class="contact" style="left:162px;top:670px">
      <svg width="10" height="10" viewBox="0 0 10 10"><circle cx="5" cy="5" r="4.3" fill="none" stroke="var(--orange)" stroke-width="1.2"/><path d="M0.7,5 H9.3 M5,0.7 C2.5,3.5 2.5,6.5 5,9.3 M5,0.7 C7.5,3.5 7.5,6.5 5,9.3" fill="none" stroke="var(--orange)" stroke-width="0.9"/></svg>
      www.rjsecuritysystems.co.uk</div>
    <div class="contact" style="left:124px;top:685px">
      <svg width="8" height="11" viewBox="0 0 8 11"><path d="M4,11 C1.5,7 0,5.5 0,4 A4,4 0 0 1 8,4 C8,5.5 6.5,7 4,11 Z" fill="var(--orange)"/><circle cx="4" cy="4" r="1.5" fill="var(--white)"/></svg>
      14 Hawthorn Lane, Fernbridge, Essex, FB7 2QL</div>

    <div class="badge-caption">Intruder Alarm<br>Systems</div>
    <div class="t review-name">TradeVouch.com</div>
    <div class="t review-tag">Trusted local reviews</div>
  </section>

  <!-- BACK PAGE -->
  <section class="page page--back">
    <svg class="shapes" width="508" height="718" viewBox="0 0 508 718">
      <defs>
        <linearGradient id="keypadPhoto" x1="0" y1="0" x2="1" y2="1">
          <stop offset="0" stop-color="#f1f2f4"/>
          <stop offset="1" stop-color="#c3c8ce"/>
        </linearGradient>
        <linearGradient id="kitPhoto" x1="0" y1="0" x2="0" y2="1">
          <stop offset="0" stop-color="#eef0f2"/>
          <stop offset="1" stop-color="#d3d7dc"/>
        </linearGradient>
        <linearGradient id="phonesPhoto" x1="0" y1="0" x2="1" y2="0">
          <stop offset="0" stop-color="#2d5f9a"/>
          <stop offset="1" stop-color="#4b7d3c"/>
        </linearGradient>
      </defs>
      <rect width="508" height="718" fill="var(--orange)"/>
      <path d="M250,0 H274 C238,120 186,248 0,322 V300 C170,230 215,110 250,0 Z" fill="var(--navy)"/>
      <path role="img" aria-label="Photo of a finger pressing a wall alarm keypad reading Welcome Home" d="M0,0 H250 C215,110 170,230 0,300 Z" fill="url(#keypadPhoto)"/>
      <polygon points="118,196 508,196 508,222 92,222" fill="var(--navy)"/>
      <path d="M0,530 C60,500 150,440 250,424 C350,410 440,404 508,402 V428 C440,430 350,436 250,452 C150,470 60,530 0,560 Z" fill="var(--navy)"/>
      <path d="M0,560 C60,530 150,470 250,452 C350,436 440,430 508,428 V718 H0 Z" fill="var(--white)"/>
      <rect role="img" aria-label="Photo of two smartphones showing a security app and live camera view" x="12" y="518" width="176" height="182" rx="10" fill="url(#phonesPhoto)"/>
      <rect role="img" aria-label="Photo of security kit: settings icon, indoor camera, smart plug and sensors" x="200" y="528" width="170" height="166" rx="8" fill="url(#kitPhoto)"/>
      <rect role="img" aria-label="Photo of a white alarm control panel" x="390" y="518" width="114" height="188" rx="6" fill="url(#kitPhoto)" stroke="#dfe2e6"/>
    </svg>

    <div class="t back-head" style="top:26px;font-size:18px;font-weight:700">R J Security Systems</div>
    <div class="t back-head" style="top:48px;font-size:18px;font-weight:300">are using the latest</div>
    <div class="t back-head" style="top:70px;font-size:22px;font-weight:700">CLOUD-BASED</div>
    <div class="t back-head" style="top:97px;font-size:22px;font-weight:700">TECHNOLOGY</div>
    <div class="t back-head" style="top:125px;font-size:17px;font-weight:300;font-style:italic;color:var(--white)">to stay connected with</div>
    <div class="t back-head" style="top:148px;font-size:17px;font-weight:700">your home and business 24/7.</div>

    <div class="t benefits-title">Some benefits of cloud services are;</div>

    <div class="benefit" style="top:233px">High level support 24/7<span class="dash"></span><svg width="11" height="11" viewBox="0 0 11 11"><circle cx="5.5" cy="5.5" r="4.6" fill="none" stroke="var(--white)" stroke-width="1.1"/><circle cx="5.5" cy="5.5" r="1.8" fill="var(--white)"/></svg></div>
    <div class="benefit" style="top:253px">Reduce engineer call outs and running costs<span class="dash"></span><svg width="11" height="11" viewBox="0 0 11 11"><circle cx="5.5" cy="3" r="2.2" fill="var(--white)"/><rect x="1.5" y="7" width="8" height="3" fill="var(--white)"/></svg></div>
    <div class="benefit" style="top:273px">Identify issues in advance<span class="dash"></span><svg width="11" height="11" viewBox="0 0 11 11"><circle cx="4.5" cy="4.5" r="3.3" fill="none" stroke="var(--white)" stroke-width="1.2"/><path d="M7,7 L10,10" stroke="var(--white)" stroke-width="1.5"/></svg></div>
    <div class="benefit" style="top:293px">Remotely manage systems to ensure correct operation<span class="dash"></span><svg width="11" height="11" viewBox="0 0 11 11"><rect x="3" y="0.5" width="5" height="10" rx="1" fill="none" stroke="var(--white)" stroke-width="1.1"/></svg></div>
    <div class="benefit" style="top:313px">Remote health checks carried out to keep your system performing as it should<span class="dash"></span><svg width="11" height="11" viewBox="0 0 11 11"><path d="M5.5,10 L1,5.5 A2.5,2.5 0 0 1 5.5,2 A2.5,2.5 0 0 1 10,5.5 Z" fill="var(--white)"/></svg></div>
    <div class="benefit" style="top:333px">Automatically update your system with the latest releases via cloud application software<span class="dash"></span><svg width="11" height="11" viewBox="0 0 11 11"><rect x="2" y="0.5" width="7" height="10" fill="none" stroke="var(--white)" stroke-width="1.1"/><path d="M3.5,3.5 H7.5 M3.5,5.5 H7.5 M3.5,7.5 H6" stroke="var(--white)" stroke-width="0.9"/></svg></div>
    <div class="benefit" style="top:353px">Interact, control and integrate your security system like never before<span class="dash"></span><svg width="12" height="10" viewBox="0 0 12 10"><path d="M3,8.5 A2.6,2.6 0 0 1 3,3.4 A3.4,3.4 0 0 1 9.4,3.8 A2.4,2.4 0 0 1 9.4,8.5 Z" fill="none" stroke="var(--white)" stroke-width="1.1"/></svg></div>

    <p class="cloud-copy">With the new cloud-based system we can check the alarm performance anytime you need it. This gives us the capability to assist you in any of your needs, be that changing user codes or system configuration. We are always there, working in the background to make sure you have the support and help you need. This is taking alarm systems into the future and leaving the stand-alone systems in the past.</p>

    <div class="t always" style="top:462px;font-size:15.5px;font-weight:700;color:var(--navy)">R J Security Systems are always</div>
    <div class="t always" style="top:480px;font-size:18px;font-weight:300;color:var(--orange)">there, always available, wherever</div>
    <div class="t always" style="top:499px;font-size:18px;font-weight:300;color:var(--orange)">and whenever you need us.</div>
  </section>

</div>
</body>
</html>
```